Business Card Design Project

My business sells promotional merchandise to large blue chip companies. Gear like polo shirts, drink bottles, pens, basically anything that you can put a company logo onto.

I need the following elements included:
Logo as attached
Peter Hollingdale Managing Director
27 Corbel Street Tarrin Cove 4178
mobile 0438 514203
email kestrelpath@kestrelpathtrading.com.au

Promotional Merchandise with a difference

Target Market(s)

Mature age Marketing Managers

Industry/Entity Type

Business

```html
<!DOCTYPE html>
<html lang="en">
<head>
<meta charset="utf-8">
<title>Kestrelpath Business Card</title>
<link rel="stylesheet" href="https://fonts.googleapis.com/css2?family=Jost:wght@300;400;500&display=swap">
<style>
  :root {
    --page: #ffffff;
    --terracotta: #925a45;
    --navy: #131a5c;
    --brand-blue: #1d2a78;
    --ink-light: #e9eaf2;
    --ink-soft: #c9cbdc;
  }
  * { margin: 0; padding: 0; box-sizing: border-box; }
  html, body {
    width: 1062px;
    height: 1200px;
    overflow: hidden;
    background: var(--page);
    font-family: "Jost", sans-serif;
  }
  .canvas { position: relative; width: 1062px; height: 1200px; }
  .card {
    position: absolute;
    left: 105px;
    width: 858px;
    height: 478px;
    overflow: hidden;
  }
  .card--front { top: 95px; background: var(--terracotta); }
  .card--back { top: 635px; background: var(--navy); color: var(--ink-light); }

  .wordmark {
    font-weight: 400;
    letter-spacing: 0.02em;
    white-space: nowrap;
    line-height: 1;
  }
  .front-wordmark {
    position: absolute;
    top: 118px;
    left: 0;
    width: 100%;
    text-align: center;
    font-size: 38px;
    color: var(--brand-blue);
  }
  .front-giant {
    position: absolute;
    left: 0;
    bottom: 0;
    width: 858px;
    height: 200px;
  }
  .front-giant text {
    font-family: "Jost", sans-serif;
    font-weight: 300;
    fill: var(--brand-blue);
  }

  .brand-block {
    position: absolute;
    top: 60px;
    right: 500px;
    text-align: right;
  }
  .back-wordmark { font-size: 36px; color: var(--ink-light); font-weight: 300; }
  .tagline {
    margin-top: 22px;
    font-size: 14px;
    line-height: 20px;
    letter-spacing: 0.12em;
    text-transform: uppercase;
    color: var(--ink-soft);
  }

  .person {
    position: absolute;
    top: 292px;
    right: 500px;
    text-align: right;
  }
  .person-name { font-size: 34px; font-weight: 400; line-height: 40px; }
  .person-role { margin-top: 6px; font-size: 23px; font-weight: 300; color: var(--ink-soft); }

  .contact {
    position: absolute;
    top: 302px;
    right: 70px;
    text-align: right;
    font-size: 19px;
    font-weight: 300;
    line-height: 25px;
    font-style: normal;
  }
</style>
</head>
<body>
<main class="canvas">
  <section class="card card--front" aria-label="Card front">
    <div class="wordmark front-wordmark">KESTRELPATH</div>
    <svg class="front-giant" viewBox="0 0 858 200" aria-hidden="true">
      <text x="0" y="197" font-size="150" textLength="858" lengthAdjust="spacingAndGlyphs">KESTRELPATH</text>
    </svg>
  </section>

  <section class="card card--back" aria-label="Card back">
    <div class="brand-block">
      <div class="wordmark back-wordmark">KESTRELPATH</div>
      <p class="tagline">Promotional merchandise<br>with a difference</p>
    </div>
    <div class="person">
      <p class="person-name">Peter Hollingdale</p>
      <p class="person-role">Managing Director</p>
    </div>
    <address class="contact">
      27 Corbel Street Tarrin Cove 4178<br>
      M: 0438 514203<br>
      E: kestrelpath@kestrelpathtrading.com.au
    </address>
  </section>
</main>
</body>
</html>
```